Security doors and flyscreens

We need business cards for our company called K & M Distributors. We quote, manufacture and install security doors and flyscreens.

Industry/Entity Type

Security

Contact Information for Business Card

K & M DISTRIBUTORS
17 Larkvale Rd. Thomastown 3074
Ph: 8157 2604
Fax: 8157 2609
Gavin: 0419 275 916
Email: gatesupplier@mailbox-example.net

```html
<!DOCTYPE html>
<html lang="en">
<head>
<meta charset="utf-8">
<title>K &amp; M Distributors – Business Card</title>
<link href="https://fonts.googleapis.com/css2?family=Saira:wght@400;500;600;700&display=swap" rel="stylesheet">
<style>
  :root {
    --page-bg: #e9ebee;
    --blue-light: #0fa3e6;
    --blue-mid: #1676d2;
    --blue-deep: #2446b0;
    --white: #ffffff;
    --paper: #f3f4f6;
    --ink-dark: #3a3e45;
    --ink-blue: #2a4aa6;
    --swoosh-grey: #5d6168;
  }
  html, body {
    margin: 0;
    padding: 0;
    width: 1200px;
    height: 900px;
    overflow: hidden;
    background: var(--page-bg);
    font-family: "Saira", sans-serif;
  }
  .canvas {
    position: relative;
    width: 1200px;
    height: 900px;
  }
  .card {
    position: absolute;
    left: 100px;
    top: 165px;
    width: 1000px;
    height: 570px;
    border-radius: 46px;
    overflow: hidden;
    box-shadow: 0 10px 30px rgba(0,0,0,0.18);
  }
  .card-art {
    position: absolute;
    inset: 0;
    width: 100%;
    height: 100%;
  }
  .brand {
    position: absolute;
    left: 62px;
    top: 150px;
    display: flex;
    align-items: center;
    gap: 18px;
  }
  .brand-mark {
    width: 64px;
    height: 64px;
    background: var(--blue-mid);
    border-radius: 6px;
  }
  .brand-name {
    font-size: 40px;
    font-weight: 700;
    color: var(--ink-dark);
    letter-spacing: 1px;
    line-height: 1;
  }
  .person {
    position: absolute;
    left: 95px;
    top: 318px;
  }
  .person-name {
    font-size: 32px;
    font-weight: 500;
    color: var(--ink-blue);
    letter-spacing: 1px;
    line-height: 1.1;
  }
  .person-title {
    font-size: 23px;
    font-weight: 600;
    color: var(--ink-dark);
    letter-spacing: 1px;
    margin-left: 18px;
  }
  .address {
    position: absolute;
    left: 75px;
    top: 478px;
    font-size: 20px;
    font-weight: 500;
    color: var(--white);
    line-height: 1.35;
  }
  .contact-list {
    position: absolute;
    right: 50px;
    top: 200px;
    margin: 0;
    padding: 0;
    list-style: none;
    text-align: right;
    color: var(--white);
    font-size: 19px;
    font-weight: 500;
    letter-spacing: 0.5px;
  }
  .contact-list li {
    display: flex;
    justify-content: flex-end;
    align-items: center;
    gap: 10px;
    height: 30px;
  }
  .contact-icon {
    width: 18px;
    height: 18px;
    flex: none;
  }
</style>
</head>
<body>
<main class="canvas">
  <section class="card" aria-label="K &amp; M Distributors business card">
    <svg class="card-art" viewBox="0 0 1000 570" preserveAspectRatio="none" aria-hidden="true">
      <defs>
        <radialGradient id="blueField" cx="0.58" cy="0.55" r="0.7">
          <stop offset="0" stop-color="#0fa3e6"/>
          <stop offset="0.6" stop-color="#1676d2"/>
          <stop offset="1" stop-color="#2446b0"/>
        </radialGradient>
        <linearGradient id="paperField" x1="0" y1="0" x2="1" y2="1">
          <stop offset="0" stop-color="#f0f1f3"/>
          <stop offset="0.5" stop-color="#ffffff"/>
          <stop offset="1" stop-color="#e8eaed"/>
        </linearGradient>
        <linearGradient id="swooshGrey" x1="0" y1="0" x2="1" y2="1">
          <stop offset="0" stop-color="#9a9ea4"/>
          <stop offset="0.5" stop-color="#5d6168"/>
          <stop offset="1" stop-color="#3c4046" stop-opacity="0.4"/>
        </linearGradient>
        <linearGradient id="bandBlue" x1="0" y1="0" x2="1" y2="0">
          <stop offset="0" stop-color="#2446b0"/>
          <stop offset="1" stop-color="#1677d3"/>
        </linearGradient>
      </defs>
      <rect class="card-base" width="1000" height="570" fill="url(#blueField)"/>
      <path class="card-paper" d="M0,0 H725 C700,230 500,420 0,465 Z" fill="url(#paperField)"/>
      <path class="card-band" d="M0,470 C200,455 330,430 430,395 C360,470 300,500 250,570 H0 Z" fill="url(#bandBlue)" opacity="0.9"/>
      <path class="card-swoosh" d="M742,0 H778 C748,210 600,360 400,420 C585,345 712,200 742,0 Z" fill="url(#swooshGrey)"/>
    </svg>

    <div class="brand">
      <span class="brand-mark"></span>
      <span class="brand-name">K &amp; M DISTRIBUTORS</span>
    </div>

    <div class="person">
      <div class="person-name">GAVIN ROWE</div>
      <div class="person-title">PRESIDENT</div>
    </div>

    <div class="address">
      17 Larkvale Rd.<br>
      Thomastown 3074
    </div>

    <ul class="contact-list">
      <li>8157 2604
        <svg class="contact-icon" viewBox="0 0 24 24" aria-hidden="true"><path fill="#fff" d="M6.6 10.8a15 15 0 0 0 6.6 6.6l2.2-2.2a1 1 0 0 1 1-.25 11.4 11.4 0 0 0 3.6.57 1 1 0 0 1 1 1V20a1 1 0 0 1-1 1A17 17 0 0 1 3 4a1 1 0 0 1 1-1h3.5a1 1 0 0 1 1 1c0 1.25.2 2.45.57 3.6a1 1 0 0 1-.25 1z"/></svg>
      </li>
      <li>0419 275 916
        <svg class="contact-icon" viewBox="0 0 24 24" aria-hidden="true"><rect x="6" y="2" width="12" height="20" rx="2" fill="none" stroke="#fff" stroke-width="2"/><circle cx="12" cy="18" r="1.2" fill="#fff"/></svg>
      </li>
      <li>8157 2609
        <svg class="contact-icon" viewBox="0 0 24 24" aria-hidden="true"><rect x="7" y="3" width="10" height="6" fill="#fff"/><rect x="3" y="9" width="18" height="9" rx="2" fill="#fff"/><rect x="7" y="15" width="10" height="6" fill="#fff" stroke="#1676d2" stroke-width="1"/></svg>
      </li>
      <li>gatesupplier@mailbox-example.net
        <svg class="contact-icon" viewBox="0 0 24 24" aria-hidden="true"><rect x="2" y="5" width="20" height="14" rx="1.5" fill="#fff"/><path d="M2.5 6 12 13l9.5-7" fill="none" stroke="#1676d2" stroke-width="1.6"/></svg>
      </li>
      <li>www.kmdistributors-example.net
        <svg class="contact-icon" viewBox="0 0 24 24" aria-hidden="true"><circle cx="12" cy="12" r="9" fill="none" stroke="#fff" stroke-width="2"/><ellipse cx="12" cy="12" rx="4" ry="9" fill="none" stroke="#fff" stroke-width="1.5"/><path d="M3 12h18M5 7h14M5 17h14" stroke="#fff" stroke-width="1.3"/></svg>
      </li>
    </ul>
  </section>
</main>
</body>
</html>
```